Need a Creative 1 Page Website Design

Looking for a personal website. This is the current site and it needs to be updated. https://corvinlestfolio.com/
Reference - glassharbor.video
meridelstudios.nyc
Use the same font used in the current site. But we need to have a more creative website
follow this order and video list https://files.pelnorashare.com/doc/7Qx2LmVtRk9aWpZc3NyHbJd4FsUe6GoYi0TnXa8Kq/edit?usp=sharing
screenshots https://files.pelnorashare.com/folders/8Rk2NxWq5TzLpVe3HbYcJ7MdUa0Gs?usp=sharing
Make a creative personal website with mostly video content.
Target Market(s)
Music
Number of Pages Required
1 page
Look and feel

```html
<!DOCTYPE html>
<html lang="en">
<head>
<meta charset="utf-8">
<title>Corvin Lest — Production</title>
<link href="https://fonts.googleapis.com/css2?family=Vollkorn:wght@600;700&family=Roboto:wght@400;500&display=swap" rel="stylesheet">
<style>
  :root {
    --red: #ef4a4f;
    --white: #ffffff;
    --footer-bg: #454545;
    --footer-link: #c9c9c9;
    --footer-muted: #6c6c6c;
  }
  * { box-sizing: border-box; margin: 0; padding: 0; }
  html, body { width: 1181px; height: 1200px; overflow: hidden; }
  body { font-family: "Roboto", Arial, sans-serif; color: var(--white); background: var(--footer-bg); }

  .hero {
    position: relative; height: 590px;
    background: linear-gradient(160deg, #3d4a55 0%, #5a4a5e 30%, #6b5a48 55%, #4e4660 78%, #3a3d48 100%);
  }
  .hero::after {
    content: ""; position: absolute; left: 0; right: 0; bottom: 0; height: 90px;
    background: linear-gradient(180deg, rgba(60,58,66,0) 0%, #3b3a42 100%);
  }
  .brand {
    font-family: "Vollkorn", Georgia, serif; font-weight: 700;
    font-size: 47px; line-height: 1; text-align: center;
  }
  .hero .brand { position: absolute; top: 16px; left: 0; right: 0; z-index: 1; }
  .play { position: absolute; left: 548px; top: 156px; z-index: 1; }

  .services {
    position: absolute; left: 74px; top: 351px; width: 1033px; height: 155px;
    display: flex; z-index: 1;
  }
  .service {
    position: relative; flex: 1; display: flex; align-items: center; justify-content: center;
    font-family: "Vollkorn", Georgia, serif; font-weight: 700; font-size: 27px;
    line-height: 1.08; text-align: center;
    text-shadow: 0 2px 6px rgba(0,0,0,.45);
  }
  .service--direction { background: linear-gradient(180deg, #6f8aa0 0%, #4f6e6a 55%, #33404a 100%); }
  .service--executive { background: linear-gradient(180deg, #5c6870 0%, #4b5a5c 60%, #3a4350 100%); }
  .service--commissioned { background: linear-gradient(180deg, #4a1a22 0%, #231a20 55%, #3a1418 100%); }
  .service + .service::before {
    content: ""; position: absolute; left: 0; top: 10px; bottom: 10px; width: 2px; background: var(--red);
  }

  .about {
    height: 443px; background: var(--red); position: relative;
  }
  .about__media {
    position: absolute; left: 74px; top: 51px; width: 492px; height: 338px;
    background: radial-gradient(ellipse at 35% 45%, #a05a9a 0%, #5a2f5c 35%, #2a1a28 75%, #1c1418 100%);
  }
  .about__body { position: absolute; left: 615px; top: 60px; width: 490px; }
  .about__title {
    font-family: "Vollkorn", Georgia, serif; font-weight: 700; font-size: 42px; line-height: 1;
  }
  .about__text { margin-top: 30px; font-size: 13.3px; line-height: 22px; }
  .about__text + .about__text { margin-top: 16px; padding-left: 3px; }
  .button {
    display: inline-flex; align-items: center; justify-content: center;
    position: absolute; left: 3px; top: 254px; width: 152px; height: 42px;
    border: 2px solid var(--white); color: var(--white); text-decoration: none;
    font-weight: 500; font-size: 14.5px;
  }

  .footer { height: 167px; background: var(--footer-bg); position: relative; }
  .footer .brand { padding-top: 18px; }
  .footer__nav { position: absolute; top: 122px; left: 0; right: 0; height: 24px; }
  .footer__nav a {
    position: absolute; top: -19px; transform: translateX(-50%); white-space: nowrap;
    color: var(--footer-link); text-decoration: none; font-size: 16.5px;
  }
  .footer__divider { position: absolute; top: -23px; width: 2px; height: 24px; background: var(--red); }
  .copyright {
    position: absolute; left: 0; right: 0; bottom: 17px; text-align: center;
    font-size: 12.5px; color: var(--footer-muted);
  }
</style>
</head>
<body>
  <header class="hero">
    <div role="img" aria-label="Background video still: a young woman in a yellow jacket walking past a graffiti-covered deli storefront" style="position:absolute;inset:0;"></div>
    <h1 class="brand">Corvin Lest</h1>
    <svg class="play" width="74" height="74" viewBox="0 0 74 74" aria-label="Play showreel">
      <circle cx="37" cy="37" r="35.5" fill="none" stroke="#fff" stroke-width="2.5"/>
      <path d="M30 23 L54 37 L30 51 Z" fill="#fff"/>
    </svg>
    <nav class="services">
      <div class="service service--direction" role="img" aria-label="Direction: music video still of an artist outdoors by a basketball court">Direction</div>
      <div class="service service--executive" role="img" aria-label="Executive Production: music video still of an artist among plants">Executive<br>Production</div>
      <div class="service service--commissioned" role="img" aria-label="Commissioned: night-time music video still with a red car">Commissioned</div>
    </nav>
  </header>

  <section class="about">
    <div class="about__media" role="img" aria-label="Camera operator filming with a rigged cinema camera in a roller rink with purple lights"></div>
    <div class="about__body">
      <h2 class="about__title">About Us</h2>
      <p class="about__text">Corvin Lest is a NYC based production Company.Lorem ipsum dolor sit amet, consectetur adipiscing elit. Mauris auctor pellentesque erat laoreet tincidunt. Suspendisse pharetra lacus id metus faucibus, ac accumsan erat luctus. Curabitur luctus in nisl ac volutpat. Cras pharetra sapien finibus odio ultricies</p>
      <p class="about__text">We would &nbsp;love to help your dreams and visions become reality.</p>
      <a class="button" href="#contact">Contact Us</a>
    </div>
  </section>

  <footer class="footer" id="contact">
    <div class="brand">Corvin Lest</div>
    <div class="footer__nav">
      <a href="#direction" style="left:400px;">Direction</a>
      <span class="footer__divider" style="left:477px;"></span>
      <a href="#executive" style="left:604px;">Executive Production</a>
      <span class="footer__divider" style="left:726px;"></span>
      <a href="#commissioned" style="left:818px;">Comissioned</a>
    </div>
    <p class="copyright">Copyright © Corvin Lest. All rights reserved.</p>
  </footer>
</body>
</html>
```